Diabetic test strips buying business needs business card

Hi all, thanks for picking up my project.

What we do is buy boxes of diabetic test strips from everyday people that are diabetics.

Many diabetes do not test all the time so they tend to have boxes left over.

This creates an opportunity for them to make some extra money by selling the boxes to us.

Here is some of the information i will want on the business card. We do not have a logo.

Name: Whitlow / Dennis
Toll Free : 1-800-555-0172

Call Today and Get Your Cash!

Website: www.tradeyourglucoseleftovers.example
Email contact@tradeyourglucoseleftovers.example

We buy diabetic test strips and pay you cash!
We accept many different brands.

Notes:

1 - Print should be readable since some diabetics have poor eyesight

2 - Sorry we do not have a logo

Please ask me any questions you have.

Thanks

Dennis
Updates

I just increase the dollar amount on my business card project.

All, i'm going to decide on the design i think is the best for me today. Please don't submit anymore designs. Thank you all for your time and great designs. Dennis

Target Market(s)

Diabetics

Industry/Entity Type

Business

Requirements
Must have
• People i would like one sir of the card to be line a mini billboard. Seems like many of the design i'm seeing are very conservative as that my be my fault for not setting the slider bar correctly.

```html
<!DOCTYPE html>
<html lang="en">
<head>
<meta charset="utf-8">
<title>Trade Your Glucose Leftovers – Business Card</title>
<link rel="stylesheet" href="https://fonts.googleapis.com/css2?family=Open+Sans:wght@400;600;700;800&display=swap">
<style>
  :root {
    --page-bg: #e4e4e4;
    --card-white: #ffffff;
    --blue-deep: #0b3f98;
    --blue-mid: #0f6cc4;
    --blue-glow: #16a6e6;
    --edge-grey: #a9adb3;
    --ink-dark: #1f1f1f;
    --ink-light: #ffffff;
  }
  * { margin: 0; padding: 0; box-sizing: border-box; }
  html, body {
    width: 1200px;
    height: 1000px;
    overflow: hidden;
    background: var(--page-bg);
    font-family: "Open Sans", Arial, sans-serif;
  }
  .sheet {
    width: 1200px;
    height: 1000px;
    display: flex;
    flex-direction: column;
    align-items: center;
    justify-content: center;
    gap: 60px;
  }
  .card {
    position: relative;
    width: 700px;
    height: 400px;
    background: var(--card-white);
    overflow: hidden;
    box-shadow: 0 6px 18px rgba(0, 0, 0, 0.18);
  }
  .card__art {
    position: absolute;
    inset: 0;
    width: 100%;
    height: 100%;
  }
  .card__name {
    position: absolute;
    left: 50px;
    top: 128px;
    font-size: 38px;
    font-weight: 700;
    color: var(--ink-dark);
    letter-spacing: 0.3px;
  }
  .card__contact {
    position: absolute;
    left: 50px;
    top: 232px;
    color: var(--ink-light);
    line-height: 1.25;
  }
  .card__tagline { font-size: 23px; font-weight: 400; }
  .card__phone { font-size: 27px; font-weight: 700; margin-bottom: 10px; }
  .card__web, .card__email { font-size: 20px; font-weight: 400; }
  .card__headline {
    position: absolute;
    left: 0;
    right: 0;
    top: 228px;
    text-align: center;
    color: var(--ink-light);
  }
  .card__brand {
    font-size: 40px;
    font-weight: 800;
    letter-spacing: 0.5px;
    text-transform: uppercase;
  }
  .card__pitch {
    font-size: 21px;
    font-weight: 400;
    line-height: 1.3;
    margin-top: 8px;
  }
</style>
</head>
<body>
<main class="sheet">

  <section class="card card--front" aria-label="Business card front">
    <svg class="card__art" viewBox="0 0 700 400" preserveAspectRatio="none" aria-hidden="true">
      <defs>
        <radialGradient id="frontBlue" cx="52%" cy="72%" r="70%">
          <stop offset="0" stop-color="var(--blue-glow)"/>
          <stop offset="0.55" stop-color="var(--blue-mid)"/>
          <stop offset="1" stop-color="var(--blue-deep)"/>
        </radialGradient>
      </defs>
      <path d="M0,214 C210,206 430,120 700,36 L700,400 L0,400 Z" fill="var(--edge-grey)"/>
      <path d="M0,222 C215,214 435,128 700,46 L700,400 L0,400 Z" fill="url(#frontBlue)"/>
    </svg>
    <h1 class="card__name">Whitlow / Dennis</h1>
    <div class="card__contact">
      <p class="card__tagline">Call Today and Get Your Cash!</p>
      <p class="card__phone">Toll Free : 1-800-555-0172</p>
      <p class="card__web">Website: www.tradeyourglucoseleftovers.example</p>
      <p class="card__email">Email contact@tradeyourglucoseleftovers.example</p>
    </div>
  </section>

  <section class="card card--back" aria-label="Business card back">
    <svg class="card__art" viewBox="0 0 700 400" preserveAspectRatio="none" aria-hidden="true">
      <defs>
        <radialGradient id="backBlue" cx="55%" cy="62%" r="70%">
          <stop offset="0" stop-color="var(--blue-glow)"/>
          <stop offset="0.55" stop-color="var(--blue-mid)"/>
          <stop offset="1" stop-color="var(--blue-deep)"/>
        </radialGradient>
      </defs>
      <path d="M0,192 C230,178 420,70 700,16 L700,400 L0,400 Z" fill="var(--edge-grey)"/>
      <path d="M0,200 C235,186 425,78 700,26 L700,400 L0,400 Z" fill="url(#backBlue)"/>
    </svg>
    <div class="card__headline">
      <h2 class="card__brand">Trade Your Glucose Leftovers</h2>
      <p class="card__pitch">We buy diabetic test strips and pay you cash!<br>We accept many different brands.</p>
    </div>
  </section>

</main>
</body>
</html>
```